Bright Horizon Painting and Remodeling needs a business card

Business card should have company logo. I will upload two different logos and let me see which one is a better design for the business card.

Name of company: Bright Horizon Painting and Remodeling
Address: 4126 NW 71st st Suite 214
Miami, FL 33166

local phone: (305) 555-0142
toll free (855) 555-0197
fax (866) 555-0163

email: corinne@paintingbrighthorizon.example

not sure if i should include social media links or names on the business card.

company does interior and exterior painting, pressure washing, wall paper removal, drywall and stucco repair, staining,

We give free estimates.

I want a two sided business card.

Not sure if all this information is necessary for the business card. Designer can pick out whatever information they deem is important for a consumer to see on the business card.

Anticipating on the business card to be printed on nice quality.

I will upload an image of one of the logos on a type of business card surface. That idea can be used as well. Be creative. Business card should be professional but very nice and eye catching.

remove drywall and stucco repair and replace with tile installation

Industry/Entity Type

Business

Contact Information for Business Card

Miami, FL 33166

toll free (855) 555-0197
fax (866) 555-0163

company does interior and exterior painting, pressure washing, wall paper removal, drywall and stucco repair, staining, tile removal, *specializing in vinyl floor removal

free estimates.

Requirements
Must have
• Profesional font

```html
<!DOCTYPE html>
<html lang="en">
<head>
<meta charset="utf-8">
<title>Bright Horizon Painting and Remodeling – Business Card</title>
<link rel="stylesheet" href="https://fonts.googleapis.com/css2?family=Open+Sans:wght@400;600&family=Merriweather:wght@700&family=Tinos&display=swap">
<style>
  :root {
    --backdrop: #e6e6e6;
    --card: #ffffff;
    --ink: #2d2d2d;
    --ink-soft: #444444;
    --accent: #8a72d6;
    --accent-soft: #c7bbef;
    --bar: #2f2b2b;
    --rule: #3a3a3a;
  }
  * { box-sizing: border-box; margin: 0; padding: 0; }
  html, body { width: 1200px; height: 987px; overflow: hidden; }
  body {
    background: var(--backdrop);
    position: relative;
    font-family: "Open Sans", Arial, sans-serif;
    color: var(--ink);
  }
  .card {
    position: absolute;
    left: 293px;
    width: 615px;
    height: 349px;
    background: var(--card);
    box-shadow: 0 2px 6px rgba(0,0,0,0.18);
    overflow: hidden;
  }
  .card--front { top: 131px; }
  .card--back { top: 506px; }

  .brand {
    position: absolute;
    font-family: "Merriweather", Georgia, serif;
    font-weight: 700;
    color: var(--ink);
    text-transform: uppercase;
    line-height: 1.25;
  }
  .brand--front {
    right: 34px; top: 62px;
    text-align: right;
    font-size: 16px;
    letter-spacing: 0.04em;
  }
  .brand--back {
    left: 0; right: 0; top: 125px;
    text-align: center;
    font-size: 28px;
    letter-spacing: 0.04em;
  }
  .brand small { display: block; font-size: 0.55em; letter-spacing: 0.2em; }

  .person { position: absolute; left: 33px; top: 148px; }
  .person__name {
    font-size: 21px; font-weight: 600; color: var(--accent);
    letter-spacing: 0.02em;
  }
  .person__role { font-size: 15px; margin-top: 2px; }

  .divider {
    position: absolute; left: 33px; right: 31px; top: 202px;
    border-top: 1px solid var(--rule);
  }

  .contacts { position: absolute; left: 33px; top: 210px; list-style: none; }
  .contacts li {
    display: flex; align-items: center; gap: 9px;
    font-size: 14px; height: 22.5px; color: var(--ink-soft);
  }
  .contacts svg { width: 14px; height: 14px; fill: var(--accent); flex: none; }

  .address {
    position: absolute; right: 34px; top: 230px;
    text-align: right; font-size: 14px; line-height: 21px;
    color: var(--ink-soft); font-style: normal;
  }

  .accent-line {
    position: absolute; left: 0; top: 329px; width: 300px; height: 8px;
    background: linear-gradient(90deg, var(--accent-soft), var(--accent));
  }
  .web-bar { position: absolute; left: 296px; top: 312px; width: 319px; height: 37px; }
  .web-front {
    position: absolute; right: 20px; top: 320px;
    font-family: "Tinos", "Times New Roman", serif;
    font-size: 15px; color: #f2f2f2; letter-spacing: 0.01em;
  }

  .socials { position: absolute; right: 18px; top: 10px; display: flex; gap: 3px; }
  .socials span {
    width: 21px; height: 21px; border-radius: 50%; background: var(--accent);
  }
  .web-back {
    position: absolute; left: 0; right: 0; top: 302px;
    text-align: center; font-size: 15px; letter-spacing: 0.4em;
    color: var(--ink-soft);
  }
</style>
</head>
<body>

<section class="card card--front" aria-label="Business card front">
  <div class="brand brand--front">Bright Horizon<small>Painting and<br>Remodeling</small></div>

  <div class="person">
    <p class="person__name">DANIEL REYES</p>
    <p class="person__role">CEO/FOUNDER</p>
  </div>
  <div class="divider"></div>

  <ul class="contacts">
    <li><svg viewBox="0 0 24 24" aria-hidden="true"><path d="M6.6 10.8a15 15 0 0 0 6.6 6.6l2.2-2.2a1 1 0 0 1 1-.25 11 11 0 0 0 3.6.6 1 1 0 0 1 1 1V20a1 1 0 0 1-1 1A17 17 0 0 1 3 4a1 1 0 0 1 1-1h3.5a1 1 0 0 1 1 1 11 11 0 0 0 .6 3.6 1 1 0 0 1-.25 1z"/></svg>(305) 555-0142</li>
    <li><svg viewBox="0 0 24 24" aria-hidden="true"><path d="M7 1h10a2 2 0 0 1 2 2v18a2 2 0 0 1-2 2H7a2 2 0 0 1-2-2V3a2 2 0 0 1 2-2zm0 3v14h10V4z"/></svg>(855) 555-0197 (T)</li>
    <li><svg viewBox="0 0 24 24" aria-hidden="true"><path d="M6 2h12v6H6zM3 9h18a1 1 0 0 1 1 1v8h-4v4H6v-4H2v-8a1 1 0 0 1 1-1zm5 7v4h8v-4z"/></svg>(866) 555-0163</li>
    <li><svg viewBox="0 0 24 24" aria-hidden="true"><path d="M2 5h20v14H2zm2 2v.5l8 5 8-5V7z"/></svg>corinne@paintingbrighthorizon.example</li>
  </ul>

  <address class="address">4126 NW 71st st<br>Suite 214<br>Miami, FL 33166</address>

  <div class="accent-line" role="img" aria-label="Accent band in the company colours"></div>
  <svg class="web-bar" viewBox="0 0 319 37" aria-hidden="true">
    <path d="M0 37 L0 14 Q2 0 16 0 L319 0 L319 37 Z" fill="var(--bar)"/>
  </svg>
  <p class="web-front">www.paintingbrighthorizon.example</p>
</section>

<section class="card card--back" aria-label="Business card back">
  <div class="socials" aria-label="Social media links"><span></span><span></span><span></span><span></span></div>
  <div class="brand brand--back">Bright Horizon<small>Painting and Remodeling</small></div>
  <p class="web-back">www.paintingbrighthorizon.example</p>
</section>

</body>
</html>
```